Lanternfield Disability - Social Security Disability Attorneys

Our company is expanding to attract clients nationwide for our social security disability practice. We have a logo, but I am looking for a creative and elegant letterhead that projects an image of being technologically advanced but still professional enough for the legal field. I am looking for the "wow factor" combined with this is still professional enough for a law practice.

Requesting letterhead and business card design
Updates

Had to update and change the logo. The previous logo had a typo. Please send updates with the new logo for consideration. The letterhead and business cards should be professional enough to be used for a law firm. Thanks.

Industry/Entity Type

Law Practice, Law Firm, Healthcare Industry, Government

Colors

Designer to choose colors to be used in the design.

Requirements
Nice to have
• **Please create a vertical design for the business card**

```html
<!DOCTYPE html>
<html lang="en">
<head>
<meta charset="utf-8">
<title>Lanternfield Disability – Business Card</title>
<link rel="stylesheet" href="https://fonts.googleapis.com/css2?family=Cinzel:wght@600;700&family=Lato:wght@400&display=swap">
<style>
  :root {
    --stage: #a3a3a3;
    --blue: #4a74e6;
    --orange: #fb832c;
    --white: #ffffff;
    --ink: #1d1d1d;
  }
  * { margin: 0; padding: 0; box-sizing: border-box; }
  html, body { width: 1200px; height: 1200px; overflow: hidden; }
  body { background: var(--stage); position: relative; font-family: 'Lato', sans-serif; }

  .card { position: absolute; top: 303px; height: 594px; overflow: hidden; }
  .card-front { left: 200px; width: 370px; background: var(--orange); }
  .card-back { left: 599px; width: 364px; background: var(--white); text-align: center; color: var(--ink); }

  .sky-band { position: absolute; left: 0; top: 0; width: 100%; height: 370px; background: var(--blue); }

  .mark-placeholder { position: absolute; display: block; }
  .front-mark { left: 140px; top: 270px; width: 90px; height: 90px; }
  .back-mark { left: 168px; top: 138px; width: 28px; height: 28px; }

  .brand-name {
    font-family: 'Cinzel', serif; font-weight: 700; letter-spacing: 1.5px; white-space: nowrap;
    text-transform: uppercase;
  }
  .brand-tagline {
    font-family: 'Cinzel', serif; font-weight: 600; font-size: 6.5px; letter-spacing: 2px; white-space: nowrap;
    text-transform: uppercase;
  }

  .front-brand { position: absolute; left: 0; width: 100%; top: 508px; text-align: center; color: var(--white); }
  .front-brand .brand-name { font-size: 18px; }
  .front-brand .brand-tagline { margin-top: 4px; }

  .back-brand { position: absolute; left: 0; width: 100%; top: 185px; color: var(--blue); }
  .back-brand .brand-name { font-size: 17px; }
  .back-brand .brand-tagline { margin-top: 5px; }

  .person { position: absolute; left: 0; width: 100%; top: 337px; }
  .person-name { font-family: 'Cinzel', serif; font-weight: 600; font-size: 23px; color: var(--blue); line-height: 1.1; text-transform: uppercase; }
  .person-role { font-size: 16px; line-height: 1.2; }

  .icon-row { position: absolute; left: 0; width: 100%; top: 396px; display: flex; justify-content: center; align-items: center; gap: 4px; }
  .icon-row .rule { width: 52px; height: 1px; background: var(--ink); margin: 0 3px; }
  .icon-row svg { width: 25px; height: 25px; display: block; }

  .contact-list { position: absolute; left: 0; width: 100%; top: 432px; font-size: 16px; line-height: 21.5px; }
  .contact-list .accent { color: var(--blue); }

  .divider { position: absolute; left: 88px; width: 195px; top: 507px; height: 1px; background: var(--ink); }

  .address { position: absolute; left: 0; width: 100%; top: 517px; font-size: 16px; line-height: 21.5px; }
</style>
</head>
<body>
  <section class="card card-front">
    <div class="sky-band"></div>
    <svg class="mark-placeholder front-mark" viewBox="0 0 90 90" role="img" aria-label="Firm logo mark">
      <circle cx="45" cy="45" r="45" fill="#ffffff"/>
    </svg>
    <div class="front-brand">
      <div class="brand-name">Lanternfield Disability</div>
      <div class="brand-tagline">Social Security Disability Attorneys</div>
    </div>
  </section>

  <section class="card card-back">
    <svg class="mark-placeholder back-mark" viewBox="0 0 28 28" role="img" aria-label="Firm logo mark">
      <circle cx="14" cy="14" r="14" fill="#fb832c"/>
    </svg>
    <div class="back-brand">
      <div class="brand-name">Lanternfield Disability</div>
      <div class="brand-tagline">Social Security Disability Attorneys</div>
    </div>

    <div class="person">
      <div class="person-name">Marcus Ellery</div>
      <div class="person-role">Managing Director</div>
    </div>

    <div class="icon-row">
      <span class="rule"></span>
      <svg viewBox="0 0 25 25" aria-label="Phone"><rect width="25" height="25" rx="3" fill="#4a74e6"/><path d="M6 11c0-3 13-3 13 0l-3 1v-2h-7v2zM8 12h9l1 6H7z" fill="#fff"/></svg>
      <svg viewBox="0 0 25 25" aria-label="Email"><rect width="25" height="25" rx="3" fill="#4a74e6"/><rect x="5.5" y="8" width="14" height="10" fill="none" stroke="#fff" stroke-width="1.3"/><path d="M5.5 8l7 6 7-6M5.5 18l5-5M19.5 18l-5-5" fill="none" stroke="#fff" stroke-width="1.1"/></svg>
      <svg viewBox="0 0 25 25" aria-label="Website"><rect width="25" height="25" rx="3" fill="#4a74e6"/><circle cx="12.5" cy="12.5" r="7" fill="#fff"/><path d="M9 8c2 1 1 3 3 3s1 3-1 3-2 2-3 1M14 16c1-2 3-1 3-3M15 7c0 2 2 2 3 3" fill="none" stroke="#4a74e6" stroke-width="1.4"/></svg>
      <span class="rule"></span>
    </div>

    <div class="contact-list">
      <div>044-555 018 274</div>
      <div>info@lanternfieldlaw.com</div>
      <div>www.<span class="accent">lanternfieldlaw</span>.com</div>
    </div>

    <div class="divider"></div>

    <div class="address">
      <div>318, Quarry Lane Suite 4</div>
      <div>60114, United States</div>
    </div>
  </section>
</body>
</html>
```